Real Estate Investor needs awesome business card design

I invest in real estate, focused on multi-family properties, and I need a business card to hand out to potential partners. I prefer simple, clean designs, but it needs to stand out, so I'd like there to be a bit of red in the design as well.

It should include this information:

Front
Dallin Pecksworth
Real Estate Investor
Direct phone: 502-867-3394
Email: dallinhpecksworth@quillmail.example
Headshot (Picture), I've uploaded a few, just pick the one you think looks best with your design. You can remove the background from the headshot image if it looks better.

Back
The back of the card's design should flow and be congruent with the front. On the back I want to put an inspirational quote or question. There will be different ones depending on the card, so I'll need the original file so I can edit it in the end.

For now, use “The Pessimist Sees Difficulty In Every Opportunity. The Optimist Sees The Opportunity In Every Difficulty.” -Barnaby Ellsworth

Target Market(s)

Investors

Industry/Entity Type

Real Estate

Contact Information for Business Card

Front
Dallin Pecksworth
Real Estate Investor

Back
The back of the card's design should flow and be congruent with the front. On the back I want to put an inspirational quote or question. There will be different ones depending on the card, so I'll need the original file so I can edit it in the end. I've uploaded some EXAMPLES of business cards with quotes on them. Don't copy but feel free to use them as inspiration.

The design will be printed on "ZIB sized" business cards
1039 x 697 pixels
with rounded corners

Font styles to use
Serif
Decorative
Script

Colors
ec1f27

Requirements
Must have
• Headshot, name, and other information in it.
• 1039 x 697 pixels
• Rounded corners
• Clean design that pops. I'm open to see any color background, including black.
• Headshots can be located here: https://www.filecrate.example/sh/8kd2wq7mzt31hvx/BBQTXP4ruf9LmQ0KhcvWx7b?dl=0
Nice to have
• It would be awesome if the design included a personal signature or monogram, but if not I'll get a personal logo developed later and the card redesigned if I think it needs it.
Should not have
• Cluttered design

```html
<!DOCTYPE html>
<html lang="en">
<head>
<meta charset="utf-8">
<title>Dallin Pecksworth – Business Card</title>
<link rel="stylesheet" href="https://fonts.googleapis.com/css2?family=Roboto+Slab:wght@300;700&family=Cormorant+Garamond:wght@400&display=swap">
<style>
  :root {
    --page-bg: #e3e6e7;
    --card-black: #1b1b1b;
    --mint: #6fd8b4;
    --mint-deep: #2f6f5a;
    --accent-red: #ec1f27;
    --photo-light: #8a8a8a;
    --photo-dark: #2a2a2a;
  }
  * { margin: 0; padding: 0; box-sizing: border-box; }
  html, body {
    width: 1200px; height: 856px; overflow: hidden;
    background: var(--page-bg);
  }
  .canvas { position: relative; width: 1200px; height: 856px; }

  .card {
    position: absolute;
    width: 560px; height: 376px;
    background: var(--card-black);
    border-radius: 28px;
    overflow: hidden;
  }
  .card--back { left: 580px; top: 40px; }
  .card--front { left: 60px; top: 440px; }

  /* Back: quote */
  .quote {
    position: absolute; left: 40px; top: 72px; right: 24px;
    font-family: "Roboto Slab", serif; font-weight: 700;
    font-size: 22px; line-height: 1.25;
    color: var(--mint);
  }
  .quote__mark {
    font-family: "Cormorant Garamond", serif;
    font-size: 38px; line-height: 0; vertical-align: -10px;
    color: var(--accent-red);
  }
  .quote__author {
    position: absolute; right: 40px; top: 236px;
    font-family: "Roboto Slab", serif; font-weight: 700;
    font-size: 19px; color: var(--mint);
  }

  /* Front: pattern panel with portrait */
  .pattern-panel {
    position: absolute; left: 0; top: 0; width: 250px; height: 376px;
    background: radial-gradient(ellipse at 50% 50%, var(--mint) 0%, var(--mint-deep) 100%);
  }
  .portrait-frame {
    position: absolute; left: 58px; top: 100px;
    width: 134px; height: 168px;
    border: 6px solid var(--mint);
    background: var(--card-black);
  }
  .portrait {
    width: 100%; height: 100%;
    background: radial-gradient(ellipse at 50% 35%, var(--photo-light), var(--photo-dark) 75%);
  }

  /* Front: details */
  .rule { position: absolute; height: 1.5px; background: var(--mint); }
  .rule--top { left: 296px; width: 190px; top: 62px; }
  .rule--name { left: 282px; width: 210px; top: 118px; background: var(--accent-red); }
  .rule--bottom { left: 300px; width: 230px; top: 262px; }
  .name {
    position: absolute; left: 284px; top: 72px;
    font-family: "Roboto Slab", serif; font-weight: 300;
    font-size: 27px; line-height: 1.2; color: var(--mint); white-space: nowrap;
  }
  .details {
    position: absolute; left: 288px; top: 188px;
    font-family: "Roboto Slab", serif; font-weight: 300;
    font-size: 13px; line-height: 1.4; color: var(--mint);
    list-style: none; white-space: nowrap;
  }
</style>
</head>
<body>
<main class="canvas">
  <section class="card card--back" aria-label="Business card back">
    <p class="quote"><span class="quote__mark">&ldquo;</span> The Pessimist Sees Difficulty<br>In Every Opportunity.<br>The Optimist Sees The Opportunity<br>In Every Difficulty <span class="quote__mark">&rdquo;</span></p>
    <p class="quote__author">Barnaby Ellsworth</p>
  </section>

  <section class="card card--front" aria-label="Business card front">
    <div class="pattern-panel" role="img" aria-label="Mint and black concentric chevron stripe pattern"></div>
    <div class="portrait-frame">
      <div class="portrait" role="img" aria-label="Black and white headshot of Dallin Pecksworth"></div>
    </div>
    <div class="rule rule--top"></div>
    <h1 class="name">Dallin Pecksworth</h1>
    <div class="rule rule--name"></div>
    <ul class="details">
      <li>Real Estate Investor</li>
      <li>Direct phone: 502-867-3394</li>
      <li>E: dallinhpecksworth@quillmail.example</li>
    </ul>
    <div class="rule rule--bottom"></div>
  </section>
</main>
</body>
</html>
```